Business card design needed

Need a simple slim business card. Wanted it in a royal or deep blue with platinum or silver writing.
Front to be to say MERIDALE EXECUTIVE CARS with website address www.mxv.com.au underneath in smaller text. Need a relevant logo to match title something elegant and classy.
At the back I would like name and then underneath mobile and email. Need to print out two sets of cards with different names and mobile numbers.
Under contact details in bullet form
*airport transfers *corporate travel *special occasions *tours
Then under that the logo and symbols of Orvanta Pay card Norvella, Kwandi card, supper guild and fleetsum.
Want all text embossed and texture of card a velvet material.
Email on back should be bookings@mxv.com.au

Email on back of card should be bookings@mxv.com.au my mistake sorry

A really dark navy blue
Elegant shiny silver writing
Must say Meridale Executive Cars on front with a logo/symbol that describes the business or business name or both?
The names on back will be seperate. So half of the cards printed will have Neil Tomack and mobile number. Next half of cards printed will have Walter Tomack and mobile. So not the 2 names on back of card.

Travel

Half card with name Neil Tomack mob 0400123987
Other half cards Walter Tomack 0400765321
Email in both bookings@meridalerides.com

```html
<!DOCTYPE html>
<html lang="en">
<head>
<meta charset="utf-8">
<title>Meridale Executive Cars – Business Card</title>
<link rel="stylesheet" href="https://fonts.googleapis.com/css2?family=Saira+Condensed:wght@300;400&family=Open+Sans:wght@400&display=swap">
<style>
  :root {
    --page-bg: #f1f1f1;
    --navy-light: #0b3d80;
    --navy-deep: #082559;
    --band: #071c46;
    --silver: #e4e8ef;
    --silver-soft: #b9c3d4;
    --accent-blue: #1a8fd9;
  }
  * { margin: 0; padding: 0; box-sizing: border-box; }
  html, body { width: 1200px; height: 1142px; overflow: hidden; }
  body {
    background: var(--page-bg);
    position: relative;
    font-family: "Saira Condensed", sans-serif;
    color: var(--silver);
  }
  .card {
    position: absolute;
    left: 228px;
    width: 768px;
    height: 413px;
    background: radial-gradient(ellipse at 15% 10%, var(--navy-light) 0%, var(--navy-deep) 75%);
    overflow: hidden;
  }
  .card--front { top: 115px; }
  .card--back { top: 642px; }

  .wordmark {
    position: absolute;
    top: 176px;
    left: 0; right: 0;
    text-align: center;
  }
  .wordmark__name {
    display: inline-block;
    font-size: 42px;
    font-weight: 400;
    letter-spacing: 0.5px;
    line-height: 1;
    padding-bottom: 4px;
    border-bottom: 4px solid var(--accent-blue);
  }
  .wordmark__url {
    margin-top: 4px;
    font-size: 28px;
    font-weight: 300;
    letter-spacing: 0.5px;
    color: var(--silver-soft);
  }

  .service-band {
    position: absolute;
    left: 0; right: 0; bottom: 0;
    height: 53px;
    background: var(--band);
    display: flex;
    align-items: center;
    justify-content: center;
    gap: 7px;
    font-family: "Open Sans", sans-serif;
    font-size: 21px;
    color: var(--silver);
    list-style: none;
  }
  .service-band li::before {
    content: "•";
    color: var(--accent-blue);
    margin-right: 3px;
  }

  .contact {
    position: absolute;
    top: 178px;
    left: 0; right: 0;
    text-align: center;
  }
  .contact__name {
    display: inline-block;
    font-size: 56px;
    font-weight: 400;
    letter-spacing: 0.5px;
    line-height: 1;
    padding-bottom: 2px;
    border-bottom: 4px solid var(--accent-blue);
  }
  .contact__line {
    font-size: 27px;
    font-weight: 300;
    letter-spacing: 0.5px;
    line-height: 1.3;
    color: var(--silver-soft);
  }
  .contact__line:first-of-type { margin-top: 6px; }

  .payment-band {
    position: absolute;
    left: 0; right: 0; bottom: 0;
    height: 73px;
    background: var(--band);
    display: flex;
    align-items: center;
    justify-content: center;
    gap: 44px;
    list-style: none;
  }
  .payment-band li {
    font-size: 24px;
    font-weight: 400;
    letter-spacing: 0.5px;
    color: var(--silver);
  }
</style>
</head>
<body>
  <section class="card card--front">
    <div class="wordmark">
      <h1 class="wordmark__name">MERIDALE EXECUTIVE CARS</h1>
      <p class="wordmark__url">www.mxv.com.au</p>
    </div>
    <ul class="service-band">
      <li>Airport transfers</li>
      <li>Corporate travel</li>
      <li>Special occasions</li>
      <li>Tours</li>
    </ul>
  </section>

  <section class="card card--back">
    <div class="contact">
      <h2 class="contact__name">Neil Tomack</h2>
      <p class="contact__line">Mob: 0400123987</p>
      <p class="contact__line">Email: bookings@mxv.com.au</p>
    </div>
    <ul class="payment-band">
      <li>Orvanta Pay</li>
      <li>Norvella</li>
      <li>Kwandi</li>
      <li>Supper Guild</li>
      <li>Fleetsum</li>
    </ul>
  </section>
</body>
</html>
```